ORK Brantell Services - Partnership Proposal

My company ORK is a study abroad consultant and We want to send a proposal to Universities and Educational institutions to partner with us. This proposal shall be used by our marketing team to collaborate with more than 100 top universities of the world and hence it must look like an extremely professional presentation.

Target Market(s)

Education institutions and Universities

Industry/Entity Type

Education

Font styles to use
Serif

Colors

Designer to choose colors to be used in the design.

Requirements
Must have
• A professional and neat look with company logo.
Nice to have
• Would like to see some the text presented in an interesting eye catchy manner.
Should not have
• Should not have too many colours or different fonts

```html
<!DOCTYPE html>
<html lang="en">
<head>
<meta charset="utf-8">
<title>ORK Brantell Services – Partnership Proposal</title>
<link rel="stylesheet" href="https://fonts.googleapis.com/css2?family=Montserrat:wght@400;600;700&family=Nunito+Sans:wght@400;600&display=swap">
<style>
:root{
  --backdrop:#5b4a3d;
  --paper:#ffffff;
  --ink:#231f20;
  --navy:#141821;
  --gold:#f2a81d;
  --gold-deep:#e59a0c;
  --rule:#f2b23a;
  --muted:#3a3a3a;
}
*{margin:0;padding:0;box-sizing:border-box}
html,body{width:1200px;height:903px;overflow:hidden;background:var(--backdrop)}
body{position:relative;font-family:"Nunito Sans",Arial,sans-serif;color:var(--ink)}
.page{position:absolute;top:146px;width:509px;height:658px;background:var(--paper);overflow:hidden;box-shadow:0 6px 18px rgba(0,0,0,.35)}
.page--cover{left:65px}
.page--inner{left:625px}
.abs{position:absolute}
.body-text{font-size:7.5px;line-height:10px;text-align:justify;color:var(--muted)}
.page-footer{position:absolute;left:0;bottom:0;width:100%;height:30px;background:var(--navy);color:#fff;font-family:"Montserrat",sans-serif;font-size:10px;letter-spacing:3px;display:flex;align-items:center;justify-content:center}

/* cover */
.cover-photo{position:absolute;left:0;top:0;width:509px;height:392px;background:linear-gradient(180deg,#4f8fd8 0%,#9cc6ee 38%,#cfd8de 62%,#3f87a8 72%,#2f7795 88%,#3c4a34 100%)}
.brand-mark{position:absolute;left:43px;top:52px;display:flex;align-items:center;gap:8px}
.brand-mark__square{width:22px;height:22px;background:var(--gold)}
.brand-mark__name{font-family:"Montserrat",sans-serif;font-weight:700;font-size:54px;line-height:1;color:#fff}
.title-band{position:absolute;left:0;top:392px;width:509px;height:73px;background:linear-gradient(90deg,var(--gold-deep),var(--gold) 50%,var(--gold-deep));text-align:center;font-family:"Montserrat",sans-serif}
.title-band__lead{font-size:24px;font-weight:400;color:var(--ink);margin-top:9px;line-height:26px;letter-spacing:.5px}
.title-band__main{font-size:23px;font-weight:700;color:#fff;line-height:26px;letter-spacing:.5px}
.why-title{font-family:"Montserrat",sans-serif;font-weight:600;font-size:9.5px;color:var(--ink)}
.why-list{list-style:none}
.why-list li{font-size:7.5px;line-height:15px;color:var(--muted);display:flex;align-items:center;gap:6px}
.why-list svg{flex:none}

/* inner */
.section-head{position:absolute;left:24px;height:16px;display:flex;align-items:center}
.section-head__label{background:var(--navy);color:#fff;font-family:"Montserrat",sans-serif;font-weight:600;font-size:10.5px;height:16px;line-height:16px;padding:0 6px}
.section-head svg{display:block}
.section-head__rule{position:absolute;top:8px;height:1px;background:var(--rule)}
.subhead{font-family:"Montserrat",sans-serif;font-weight:600;font-size:9.4px;color:var(--ink)}
.person-name{font-family:"Montserrat",sans-serif;font-weight:600;font-size:9.4px;color:var(--ink)}
.reason{display:flex;gap:7px}
.reason__num{flex:none;width:9px;height:9px;border-radius:50%;background:var(--gold);color:var(--ink);font-size:6.5px;font-weight:600;text-align:center;line-height:9px;margin-top:1px}
.social{font-family:"Montserrat",sans-serif;font-size:9px;font-weight:600;color:var(--ink);display:flex;align-items:center;gap:6px;line-height:16px}
.social__square{width:9px;height:9px;background:#3b5c9a}
.social__square--alt{background:#3aa3e0}
.brand-small{position:absolute;left:382px;top:578px;display:flex;align-items:center;gap:5px}
.brand-small__square{width:9px;height:9px;background:var(--gold)}
.brand-small__name{font-family:"Montserrat",sans-serif;font-weight:700;font-size:28px;line-height:1;color:var(--navy)}
</style>
</head>
<body>

<section class="page page--cover">
  <div class="cover-photo" role="img" aria-label="Photograph of a harbour city skyline with a tall tower, blue sky with clouds, water with a ferry and sailboat"></div>
  <div class="brand-mark">
    <span class="brand-mark__name">ORK</span>
    <span class="brand-mark__square"></span>
  </div>
  <div class="title-band">
    <p class="title-band__lead">PROPOSAL TO</p>
    <p class="title-band__main">REPRESENT YOUR INSTITUTION</p>
  </div>

  <div class="abs" style="left:23px;top:475px;width:218px">
    <p class="body-text">ORK Brantell Services Limited is a New Zealand based company established in 2013, engaged in providing end-to-end study abroad and migration services to international students and families. Headed by a Licensed Immigration Adviser with a strong social media presence and a sales &amp; service team operating from different parts of the world. ORK has been servicing clients from more than 30 countries of the world like India, Sri Lanka, Maldives, UAE, Egypt, Brazil, etc. The company boasts of being a specialist in New Zealand student enrollment and also offers after arrival support by an experienced and efficient onshore team.</p>
    <p class="body-text" style="margin-top:10px">ORK is proud to have successfully served all the leading New Zealand Institutions.</p>
  </div>

  <div class="abs" style="left:261px;top:475px;width:225px">
    <p class="body-text">Having spent over a decade in this pursuit and realizing the ever increasing growth of study abroad aspirants, the core team of ORK is now keen to expand into other countries and set a global footprint in overseas education domain. Our consistent and creative social media marketing initiatives are attracting topnotch students from different countries to study in high quality global institutions.</p>
    <p class="why-title" style="margin-top:7px;margin-bottom:4px">Why partner with us?</p>
    <ul class="why-list">
      <li><svg width="6" height="6" viewBox="0 0 6 6"><rect x=".5" y=".5" width="5" height="5" fill="none" stroke="#f2a81d"/><path d="M1.4 3l1.1 1.1L4.7 1.7" fill="none" stroke="#f2a81d" stroke-width=".8"/></svg>Proven track record of student enrollment for New Zealand</li>
      <li><svg width="6" height="6" viewBox="0 0 6 6"><rect x=".5" y=".5" width="5" height="5" fill="none" stroke="#f2a81d"/><path d="M1.4 3l1.1 1.1L4.7 1.7" fill="none" stroke="#f2a81d" stroke-width=".8"/></svg>High conversion rate - application to enrolment</li>
      <li><svg width="6" height="6" viewBox="0 0 6 6"><rect x=".5" y=".5" width="5" height="5" fill="none" stroke="#f2a81d"/><path d="M1.4 3l1.1 1.1L4.7 1.7" fill="none" stroke="#f2a81d" stroke-width=".8"/></svg>Qualified and experienced team across countries</li>
    </ul>
  </div>

  <footer class="page-footer">www.orkbrantell.com</footer>
</section>

<section class="page page--inner">
  <div class="section-head" style="top:25px">
    <span class="section-head__label">Our approach and benefit to your institution</span>
    <svg width="9" height="16" viewBox="0 0 9 16"><path d="M1 0h3l5 16H6z" fill="#f2a81d"/></svg>
  </div>
  <div class="section-head__rule" style="left:284px;width:201px;top:33px"></div>
  <p class="subhead abs" style="left:24px;top:48px">We are expanding beyond attracting students to New Zealand due to the following reasons:</p>

  <div class="reason abs" style="left:24px;top:66px;width:221px">
    <span class="reason__num">1</span>
    <p class="body-text">The number of international students coming to New Zealand at both the high school and tertiary level is approximately 140,000 annually and increasing consistently. Some of them seek to move into institutions such as your institution after completion of their courses in New Zealand because they are either not able to get an admission into a New Zealand university since there are only 8 of them. Or they are simply keen to move into a larger country having experienced new Zealand (see results of a survey we conducted). There are limited agencies in New Zealand assisting in such a move and we aim to fill this gap in the market. This is our mutual opportunity to tap into a whole new segment of potential international students moving between countries.</p>
  </div>
  <div class="reason abs" style="left:263px;top:66px;width:222px">
    <span class="reason__num">2</span>
    <p class="body-text">When we recruit students for New Zealand institutions from our main markets, most of them seek to have a 2nd option of a different country and an institution like your institution. Eventually a significant number choose not to go to New Zealand and we would like to offer them more options. This is the other reason we are embarking on this expansion and reaching out to you.</p>
  </div>
  <div class="reason abs" style="left:263px;top:156px;width:222px">
    <span class="reason__num">3</span>
    <p class="body-text">Considering XYZ University has courses which can be very attractive to the above set of students, we will be delighted to partner with you. Bolstered by your exceptional student credentials and our professional focus we foresee a good partnership.</p>
  </div>

  <div class="section-head" style="top:229px">
    <span class="section-head__label">Additional support to our students</span>
    <svg width="9" height="16" viewBox="0 0 9 16"><path d="M1 0h3l5 16H6z" fill="#f2a81d"/></svg>
  </div>
  <div class="section-head__rule" style="left:228px;width:257px;top:237px"></div>
  <p class="body-text abs" style="left:24px;top:251px;width:461px">Our New Zealand success rides firmly on the onshore support we provide to our students once they arrive here. We aim to create the same model in your country as well as soon as active recruitment starts. We will be appointing an onshore adviser in your country who together with the your institution team will create a robust partnership between institution and agent to support our students.</p>

  <div class="section-head" style="top:307px">
    <span class="section-head__label">The team and advisers</span>
    <svg width="9" height="16" viewBox="0 0 9 16"><path d="M1 0h3l5 16H6z" fill="#f2a81d"/></svg>
  </div>
  <div class="section-head__rule" style="left:166px;width:319px;top:315px"></div>

  <p class="person-name abs" style="left:24px;top:332px">Daniel Marsh, Director -</p>
  <p class="body-text abs" style="left:24px;top:349px;width:221px">He holds a Bachelor of Commerce with honors degree as well as a GCNZEA from Harbourline Polytechnic. He has a full license to practice as a Licensed Immigration Adviser and is based in Hamilton, New Zealand. He was a chairperson of Southern Cross Specialist Agents (SCSA), the elite group of education agents formed under the aegis of Study Aotearoa. He was accorded the privilege of a private audience with His Excellency the Governor General of New Zealand in recognition of his services towards the promotion of New Zealand education.</p>

  <p class="person-name abs" style="left:266px;top:332px">Helen Carwright -</p>
  <p class="body-text abs" style="left:265px;top:350px;width:220px">With a background in teaching, academic and marketing roles Helen has a wealth of experience and knowledge to reflect on and actively mentor our future growth. She worked for 24 years in New Zealand Government tertiary institutions as a Lecturer, Head of Department, Business Liaison Manager, International Manager and International Marketing Manager. She has qualifications from Kauri Coast University and Ellsworth University.</p>

  <p class="person-name abs" style="left:24px;top:464px">Dr Peter Lindqvist -</p>
  <p class="body-text abs" style="left:24px;top:479px;width:221px">Dr Lindqvist is a former Policy Officer with the Pacific Commerce Bureau as well as the Southern Overseas Relations Office. He was also a MBA lecturer in international trade and global enterprise. With this plethora of experience and knowledge he is an invaluable member of our advisory board and plays an important and active role in our future growth.</p>

  <p class="body-text abs" style="left:265px;top:469px;width:220px">Other team members based in India include 20 education advisers/counsellors and 6 visa processing staff and together they manage the entire student process from enquiry to a successful visa application. They are competent with the processes for all countries.</p>

  <div class="section-head" style="top:563px">
    <span class="section-head__label">Conclusion</span>
    <svg width="9" height="16" viewBox="0 0 9 16"><path d="M1 0h3l5 16H6z" fill="#f2a81d"/></svg>
  </div>
  <p class="body-text abs" style="left:24px;top:585px;width:221px">We are confident in our ability to create a mutually successful, meaningful and sustainable partnership with your institution. We look forward to the opportunity.</p>

  <div class="abs" style="left:283px;top:584px">
    <p class="social"><span class="social__square"></span>@ORK_kiwi</p>
    <p class="social"><span class="social__square social__square--alt"></span>@ORK_kiwi</p>
  </div>
  <div class="brand-small">
    <span class="brand-small__name">ORK</span>
    <span class="brand-small__square"></span>
  </div>

  <footer class="page-footer">www.orkbrantell.com</footer>
</section>

</body>
</html>
```